BRINEWAKE DIVE

IM LOOKING AT A BROCHURE MY MY DIVE CENTRE WE DO COURSES FROM INTRO TO PROFESSIONAL, IM OPEN TO DESIGN AND COLOURS, JUST LOOKING FOR SOMETHING THAT STANDS OUT.

i HAVE INCLUDED A COPY OF OUR LAST BROCHURE SO YOU CAN SEE THE INFORMATION THAT WE PREVIOUSLY USED AND ALSO OUR PRICING.

WE HAVE MANY DIVE COMPANY'S IN NORTH QUEENSLAND AND THROUGHOUT AUSTRALIA, WE ARE AFTER SOMETHING THAT PEOPLE ARE DRAWN TO AND WILL STAND OUT AMONGST OTHER COMPETITORS.

LOOKING FOR PLAYFUL AND FUN

```html
<!DOCTYPE html>
<html lang="en">
<head>
<meta charset="utf-8">
<title>Brinewake Dive – Courses</title>
<link href="https://fonts.googleapis.com/css2?family=Open+Sans:wght@400;600;700&display=swap" rel="stylesheet">
<style>
:root{
  --navy:#2c3a86;
  --navy-deep:#262f72;
  --aqua:#7fd3e6;
  --aqua-light:#b7e8f2;
  --teal:#5fc7b4;
  --reef-dark:#0f3d4a;
  --reef-mid:#1f6f7c;
  --card:#ffffffe8;
  --ink:#2a2f55;
  --white:#ffffff;
  --page:#9a9a9a;
}
*{margin:0;padding:0;box-sizing:border-box}
html,body{width:1200px;height:800px;overflow:hidden;background:var(--page)}
body{font-family:"Open Sans",Arial,sans-serif;position:relative}
.brochure{position:absolute;left:0;top:0;width:1200px;height:800px;overflow:hidden}
.cover-panel{position:absolute;left:0;top:0;width:400px;height:800px;
  background:linear-gradient(180deg,var(--reef-dark) 0%,var(--reef-mid) 35%,#4f7f86 60%,#5b6670 100%)}
.brand{position:absolute;left:60px;top:70px;width:280px;text-align:center;color:var(--white)}
.brand-dot{width:70px;height:70px;border-radius:50%;background:var(--white);margin:0 auto 12px}
.brand-name{font-weight:700;font-size:30px;letter-spacing:.5px}
.brand-tagline{font-weight:600;font-size:14px;margin-top:4px;color:var(--teal)}
.diver-photo{position:absolute;left:70px;top:300px;width:280px;height:500px;
  background:linear-gradient(180deg,#8a9aa0 0%,#5f6a70 50%,#3a4046 100%);border-radius:120px 120px 0 0}
.inside{position:absolute;left:400px;top:0;width:800px;height:800px}
.reef-top{position:absolute;left:0;top:0;width:800px;height:520px;
  background:linear-gradient(180deg,var(--aqua) 0%,var(--aqua-light) 60%,#9fd9e6 100%)}
.navy-band{position:absolute;left:0;top:450px;width:800px;height:350px;
  background:linear-gradient(180deg,var(--navy) 0%,#3e5aa0 55%,var(--navy) 100%)}
.teal-stripe{position:absolute;left:0;top:700px;width:800px;height:18px;background:var(--teal)}
.navy-foot{position:absolute;left:0;top:718px;width:800px;height:82px;background:var(--navy-deep)}
.price-card{position:absolute;left:40px;top:60px;width:710px;height:440px;background:var(--card);
  border-radius:18px;overflow:hidden;color:var(--ink)}
.price-head{height:40px;background:var(--navy);display:flex;justify-content:space-between;align-items:flex-end;padding:0 22px 8px}
.price-head span{color:var(--aqua);font-weight:700;font-size:16px}
.price-head .price-label{color:var(--white)}
.price-table{width:100%;border-collapse:collapse;margin-top:12px;font-size:14.5px}
.price-table td{padding:1.5px 22px;line-height:19px;vertical-align:top}
.price-table td.amount{text-align:right;white-space:nowrap}
.price-note{position:absolute;left:22px;bottom:14px;font-size:12px}
.about{position:absolute;left:60px;top:530px;width:700px;color:var(--white);font-size:14.5px;line-height:21px}
.about p+p{margin-top:14px}
</style>
</head>
<body>
<div class="brochure">
  <section class="cover-panel">
    <div class="brand">
      <div class="brand-dot"></div>
      <div class="brand-name">Brinewake Dive</div>
      <div class="brand-tagline">Go under, down under</div>
    </div>
    <div class="diver-photo" role="img" aria-label="Photo of a scuba diver in a wetsuit and dive gear, lifting a mask, in front of a coral reef"></div>
  </section>

  <section class="inside">
    <div class="reef-top" role="img" aria-label="Underwater reef scene with tropical fish"></div>
    <div class="navy-band"></div>
    <div class="teal-stripe"></div>
    <div class="navy-foot"></div>

    <div class="price-card">
      <div class="price-head"><span>COURSE</span><span class="price-label">Price</span></div>
      <table class="price-table">
        <tr><td>Introductory Discover Scuba Diving</td><td class="amount">$75</td></tr>
        <tr><td>Repeat Introductory Discover Scuba Diving</td><td class="amount">$60</td></tr>
        <tr><td>Scuba Diver Course</td><td class="amount">$260</td></tr>
        <tr><td>Open Water Diver Course (excluding accommodation)</td><td class="amount">$350</td></tr>
        <tr><td>Open Water Diver Course<br>(including 4 nights accommodation at Harbour backpackers)</td><td class="amount">$399</td></tr>
        <tr><td>Advanced Open Water Diver Course<br>(including 2 nights accommodation at Harbour backpackers)</td><td class="amount">$520</td></tr>
        <tr><td>Rescue Diver Course</td><td class="amount">$499</td></tr>
        <tr><td>Divemaster/Dive Control Specialist Course</td><td class="amount">POA</td></tr>
        <tr><td>Certified Dive</td><td class="amount">$60</td></tr>
        <tr><td>Repeat Certified Dive</td><td class="amount">$40</td></tr>
        <tr><td>Refresher Course</td><td class="amount">$95</td></tr>
        <tr><td>Night Dive</td><td class="amount">$75</td></tr>
        <tr><td>Full Day Diving equipment hire</td><td class="amount">$55</td></tr>
        <tr><td>Full Day Snorkel equipment hire</td><td class="amount">$15</td></tr>
      </table>
      <p class="price-note">Prices exclude Reef tax and all courses are subject to a dive medical and weather conditions.</p>
    </div>

    <div class="about">
      <p>Brinewake Dive is based on the beautiful Saltmere Island located within 25 minutes from Coralport, the largest City in far North Queensland. You can find us in the heart of Harbour backpackers which is in the picturesque Kelp Bay. At Brinewake Dive we have our dive pool only steps away from the classroom with stunning views to the ocean and the spectacular Kelp Bay.</p>
      <p>We offer a range of courses for beginners through to professional dive qualifications. The dive centre is fully stocked with modern training materials and facilities. We pride ourselves on our calm, safe and laid back teaching environment.</p>
    </div>
  </section>
</div>
</body>
</html>
```